oneness poster

a clean, elegant, simple text poster as follows (with some sort of glow or background consistent with the message:
MANIFESTO OF QUIET RIVERS

1. I am part of the world. The world is not outside of me, and I am not outside of the world. The world is in me, and I am in the world.

2. I am part of nature, and nature is part of me. I am what I am in my communication and communion with all living things. I am an irreducible and coherent whole with the web of life on the planet.

3. I am part of society, and society is part of me. I am what I am in my communication and communion with my fellow humans. I am an irreducible and coherent whole with the community of humans on the planet.

4. I am more than a skin-and-bone material organism: my body, and its cells and organs are manifestations of what is truly me: a self-sustaining, self-evolving dynamic system arising, persisting and evolving in interaction with everything around me.

5. I am one of the highest, most evolved manifestations of the drive toward coherence and wholeness in the universe. All systems drive toward coherence and wholeness in interaction with all other systems, and my essence is this cosmic drive. It is the same essence, the same spirit that is inherent in all the things that arise and evolve in nature, whether on this planet or elsewhere in the infinite reaches of space and time.

6. There are no absolute boundaries and divisions in this world, only transition points where one set of relations yields prevalence to another. In me, in this self-maintaining and self-evolving coherence- and wholeness-oriented system, the relations that integrate the cells and organs of my body are prevalent. Beyond my body other relations gain prevalence: those that drive toward coherence and wholeness in society and in nature.

7. The separate identity I attach to other humans and other things is but a convenient convention that facilitates my interaction with them. My family and my community are just as much “me” as the organs of my body. My body and mind, my family and my community, are interacting and interpenetrating, variously prevalent elements in the network of relations that encompasses all things in nature and the human world.

8. The whole gamut of concepts and ideas that separates my identity, or the identity of any person or community, from the identity of other persons and communities are manifestations of this convenient but arbitrary convention. There are only gradients distinguishing individuals from each other and from their environment and no real divisions and boundaries. There are no “others” in the world: we are all living systems and we are all part of each other.

9. Attempting to maintain the system I know as “me” through ruthless competition with the system I know as “you” is a grave mistake: it could damage the integrity of the embracing whole that frames both your life and mine. I cannot preserve my own life and wholeness by damaging that whole, even if damaging a part of it seems to bring me short-term advantage. When I harm you, or anyone else around me, I harm myself.

10. Collaboration, not competition, is the royal road to the wholeness that hallmarks healthy systems in the world. Collaboration calls for empathy and solidarity, and ultimately for love. I do not and cannot love myself if I do not love you and others around me: we are part of the same whole and so are part of each other.

11. The idea of “self-defense” even of “national defense,” needs to be rethought. Patriotism if it aims to eliminate adversaries by force, and heroism even in the well-meaning execution of that aim, are mistaken aspirations. A patriot and a hero who brandishes a sword or a gun is an enemy also to himself. Every weapon intended to hurt or kill is a danger to all. Comprehension, conciliation and forgiveness are not signs of weakness; they are signs of courage.

12. “The good” for me and for every person in the world is not the possession and accumulation of personal wealth. Wealth, in money or in any material resource, is but a means for maintaining myself in my environment. As exclusively mine, it commandeers part of the resources that all things need to share if they are to live and to thrive. Exclusive wealth is a threat to all people in the human community. And because I am a part of this community, in the final count it is a threat also to me, and to all who hold it.

13. Beyond the sacred whole we recognize as the world in its totality, only life and its development have what philosophers call intrinsic value; all other things have merely instrumental value: value insofar as they add to or enhance intrinsic value. Material things in the world, and the energies and substances they harbor or generate, have value only if and insofar they contribute to life and wellbeing in the web of life on this Earth.

14. Every healthy person has pleasure in giving: it is a higher pleasure than having. I am healthy and whole when I value giving over having. The true measure of my accomplishment and excellence is my readiness to give. Not the amount of what I give is the measure of my accomplishment and excellence, but the relation between what I give, and what my family and I need to live and to thrive.

15. A community that values giving over having is a community of healthy people, oriented toward thriving through empathy, solidarity, and love among its members. Sharing enhances the community of life, while possessing and accumulating creates demarcation, invites competition, and fuels envy. The share-society is the norm for all the communities of life on the planet; the have-society is typical only of modern-day humanity, and it is an aberration.
.

16. I acknowledge my role and responsibility in evolving a planetary consciousness in me, and by example in others around me. I have been part of the aberration of human consciousness in the modern age, and now wish to become part of the evolution that overcomes the aberration and heals the wounds inflicted by it. This is my right as well as my duty, as a conscious member of a conscious species on a precious and now critically endangered planet.

• MANIFESTO OF QUIET RIVERS

.

• a very very simple glow in the background or other look consistent with the all-is-one (OM) message. A strong, almost spirtual feel.
• no flowery designs, no distractions. Nothing cute.

```html
<!DOCTYPE html>
<html lang="en">
<head>
<meta charset="utf-8">
<title>Manifesto of Quiet Rivers</title>
<link rel="stylesheet" href="https://fonts.googleapis.com/css2?family=Bebas+Neue&family=Source+Sans+3:wght@400;700&display=swap">
<style>
  :root {
    --ink: #1f1f1f;
    --accent: #d1242b;
    --bg-light: #f4f4f7;
    --bg-mid: #d9d9df;
    --bg-dark: #b9b9c2;
    --glow: rgba(255, 255, 255, 0.75);
  }
  html, body {
    margin: 0;
    padding: 0;
    width: 850px;
    height: 1200px;
    overflow: hidden;
    background: var(--bg-mid);
  }
  .poster {
    position: relative;
    width: 850px;
    height: 1200px;
    overflow: hidden;
    background:
      radial-gradient(ellipse 60% 45% at 50% 48%, var(--bg-light) 0%, rgba(244,244,247,0) 70%),
      linear-gradient(180deg, var(--bg-dark) 0%, var(--bg-mid) 35%, var(--bg-light) 60%, var(--bg-mid) 85%, var(--bg-dark) 100%);
    color: var(--ink);
  }
  .poster__glow {
    position: absolute;
    inset: 0;
    background:
      radial-gradient(circle 150px at 82% 22%, var(--glow), rgba(255,255,255,0) 100%),
      radial-gradient(circle 120px at 58% 38%, rgba(255,255,255,0.55), rgba(255,255,255,0) 100%),
      radial-gradient(circle 110px at 30% 68%, rgba(255,255,255,0.5), rgba(255,255,255,0) 100%),
      radial-gradient(circle 90px at 82% 92%, rgba(255,255,255,0.5), rgba(255,255,255,0) 100%);
  }
  .poster__title {
    position: absolute;
    top: 14px;
    left: 0;
    width: 100%;
    margin: 0;
    text-align: center;
    font-family: "Bebas Neue", "Oswald", sans-serif;
    font-weight: 400;
    font-size: 70px;
    line-height: 70px;
    letter-spacing: -0.5px;
    color: var(--ink);
  }
  .poster__title-accent {
    color: var(--accent);
  }
  .tenets {
    position: absolute;
    top: 103px;
    left: 0;
    right: 0;
    margin: 0;
    padding: 0 0 0 17px;
    list-style: none;
    counter-reset: tenet;
    font-family: "Source Sans 3", "Myriad Pro", sans-serif;
    font-weight: 700;
    font-size: 12.7px;
    line-height: 17.4px;
  }
  .tenets__item {
    position: relative;
    counter-increment: tenet;
    margin: 0 0 10.7px 0;
    white-space: nowrap;
  }
  .tenets__item::before {
    content: counter(tenet) ".";
    position: absolute;
    left: -13px;
    font-size: 9px;
    font-weight: 400;
  }
</style>
</head>
<body>
<main class="poster">
  <div class="poster__glow" role="img" aria-label="Soft white light circles glowing over a pale grey field"></div>

  <h1 class="poster__title">MANIFESTO OF QUIET <span class="poster__title-accent">RIVERS</span></h1>

  <ol class="tenets">
    <li class="tenets__item">I am part of the world, The world is not outside of me, and I am not outside of the world. The world is in me, and I am in the world.</li>
    <li class="tenets__item">I am part of nature, and nature is part of me, I am what I am in my communication and communion with all living things. I am an<br>irreducible and coherent whole with the web of life on the planet.</li>
    <li class="tenets__item">I am part of society, and society is part of me, I am what I am in my communication and communion with my fellow humans. I am an irreducible<br>and coherent whole with the community of humans on the planet.</li>
    <li class="tenets__item">I am more than a skin-and-bone material organism my body, and its cells and organs are manifestations of what is truly me: a self-sustaining,<br>self-evolving dynamic system arising, persisting and evolving in interaction with everything around me.</li>
    <li class="tenets__item">I am one of the highest most evolved manifestations of the drive toward coherence and wholeness in the universe.<br>All systems drive toward coherence and wholeness in interaction with all other systems, and my essence is this cosmic drive.<br>It is the same essence, the same spirit that is inherent in all the things that arise and evolve in nature, whether on this planet or elsewhere in the<br>infinite reaches of space and time.</li>
    <li class="tenets__item">There are no absolute boundaries and divisions in this world only transition points where one set of relations yields prevalence to another.<br>In me, in this self-maintaining and self-evolving coherence- and wholeness-oriented system, the relations that integrate the cells and organs<br>of my body are prevalent. Beyond my body other relations gain prevalence: those that drive toward coherence and wholeness in society<br>and in nature.</li>
    <li class="tenets__item">The separate identity I attach to other humans and other things is but a convenient convention that facilitates my interaction with them.<br>My family and my community are just as much “me” as the organs of my body. My body and mind, my family and my community, are interacting<br>and interpenetrating, variously prevalent elements in the network of relations that encompasses all things in nature and the human world.</li>
    <li class="tenets__item">The whole gamut of concepts and ideas that separates my identity, or the identity of any person or community, from the identity of other persons<br>and communities are manifestations of this convenient but arbitrary convention. There are only gradients distinguishing individuals<br>from each other and from their environment and no real divisions and boundaries. There are no “others” in the world: we are all living systems<br>and we are all part of each other.</li>
    <li class="tenets__item">Attempting to maintain the system I know as “me” through ruthless competition with the system I know as “you” is a grave mistake:<br>it could damage the integrity of the embracing whole that frames both your life and mine. I cannot preserve my own life and wholeness<br>by damaging that whole, even if damaging a part of it seems to bring me short-term advantage. When I harm you, or anyone else around me,<br>I harm myself.</li>
    <li class="tenets__item">Collaboration, not competition, is the royal road to the wholeness that hallmarks healthy systems in the world. Collaboration calls for empathy<br>and solidarity, and ultimately for love. I do not and cannot love myself if I do not love you and others around me: we are part of the same whole<br>and so are part of each other.</li>
    <li class="tenets__item">The idea of “self-defense” even of “national defense,” needs to be rethought. Patriotism if it aims to eliminate adversaries by force, and heroism<br>even in the well-meaning execution of that aim, are mistaken aspirations. A patriot and a hero who brandishes a sword or a gun is an enemy<br>also to himself. Every weapon intended to hurt or kill is a danger to all. Comprehension, conciliation and forgiveness are not signs of weakness;<br>they are signs of courage.</li>
    <li class="tenets__item">“The good” for me and for every person in the world is not the possession and accumulation of personal wealth. Wealth, in money<br>or in any material resource, is but a means for maintaining myself in my environment. As exclusively mine, it commandeers part of the resources<br>that all things need to share if they are to live and to thrive. Exclusive wealth is a threat to all people in the human community.<br>And because I am a part of this community, in the final count it is a threat also to me, and to all who hold it.</li>
    <li class="tenets__item">Beyond the sacred whole we recognize as the world in its totality, only life and its development have what philosophers call intrinsic value;<br>all other things have merely instrumental value: value insofar as they add to or enhance intrinsic value. Material things in the world,<br>and the energies and substances they harbor or generate, have value only if and insofar they contribute to life and well being in the web of life<br>on this Earth.</li>
    <li class="tenets__item">Every healthy person has pleasure in giving: it is a higher pleasure than having. I am healthy and whole when I value giving over having. The true<br>measure of my accomplishment and excellence is my readiness to give. Not the amount of what I give is the measure of my accomplishment and<br>excellence, but the relation between what I give, and what my family and I need to live and to thrive.</li>
    <li class="tenets__item">A community that values giving over having is a community of healthy people, oriented toward thriving through empathy, solidarity,<br>and love among its members. Sharing enhances the community of life, while possessing and accumulating creates demarcation,<br>invites competition, and fuels envy. The share-society is the norm for all the communities of life on the planet; the have-society is typical<br>only of modern-day humanity, and it is an aberration.</li>
    <li class="tenets__item">I acknowledge my role and responsibility in evolving a planetary consciousness in me, and by example in others around me. I have been<br>part of the aberration of human consciousness in the modern age, and now wish to become part of the evolution that overcomes the aberration<br>and heals the wounds inflicted by it. This is my right as well as my duty, as a conscious member of a conscious species on a precious<br>and now critically endangered planet.</li>
  </ol>
</main>
</body>
</html>
```